Business Card For Life Coaching Business For Men

Take my existing logo and apply it to a business card. I would like the logo to be prominent with stylistic text below reading Life Coaching For Men. Contact info should show as:
Dale Hartwig
dale@steadforgepath.com

```html
<!DOCTYPE html>
<html lang="en">
<head>
<meta charset="UTF-8">
<title>Steadforge Path — Business Card</title>
<link href="https://fonts.googleapis.com/css2?family=Oswald:wght@400;500&family=Roboto:wght@400&display=swap" rel="stylesheet">
<style>
  :root {
    --navy: #0a0a8c;
    --teal: #0e8080;
    --slate: #7b98b8;
    --white: #ffffff;
    --ink: #2a2a33;
    --backdrop: #e9e7e3;
  }
  * { margin: 0; padding: 0; box-sizing: border-box; }
  html, body { width: 1200px; height: 900px; overflow: hidden; }
  body {
    background: var(--backdrop);
    display: flex;
    flex-direction: column;
    align-items: center;
    justify-content: center;
    gap: 40px;
  }
  .card {
    position: relative;
    width: 700px;
    height: 400px;
    overflow: hidden;
    box-shadow: 0 6px 18px rgba(0,0,0,0.18);
  }
  .card-front {
    background: var(--navy);
    display: flex;
    align-items: center;
    justify-content: center;
  }
  .brand {
    display: flex;
    align-items: center;
    gap: 22px;
  }
  .brand-dot {
    width: 110px;
    height: 110px;
    border-radius: 50%;
    background: var(--teal);
    flex: none;
  }
  .brand-text { display: flex; flex-direction: column; }
  .brand-name {
    font-family: "Oswald", sans-serif;
    font-weight: 500;
    text-transform: uppercase;
    line-height: 0.95;
    letter-spacing: -0.5px;
  }
  .brand-tagline {
    font-family: "Oswald", sans-serif;
    font-weight: 400;
    text-transform: uppercase;
    letter-spacing: 2px;
    color: var(--teal);
    white-space: nowrap;
  }
  .card-front .brand-name { color: var(--white); font-size: 62px; }
  .card-front .brand-tagline { font-size: 19px; margin-top: 10px; letter-spacing: 3px; }

  .card-back { background: var(--white); }
  .holder-name {
    position: absolute;
    left: 58px;
    top: 62px;
    font-family: "Oswald", sans-serif;
    font-weight: 500;
    font-size: 38px;
    text-transform: uppercase;
    letter-spacing: -0.5px;
  }
  .holder-first { color: var(--navy); }
  .holder-last { color: var(--teal); }
  .card-back .brand {
    position: absolute;
    right: 40px;
    top: 44px;
    gap: 14px;
  }
  .card-back .brand-dot { width: 62px; height: 62px; }
  .card-back .brand-name { color: var(--navy); font-size: 34px; }
  .card-back .brand-tagline { font-size: 11px; margin-top: 6px; }

  .contact-list {
    position: absolute;
    left: 58px;
    top: 220px;
    list-style: none;
    font-family: "Roboto", sans-serif;
    font-size: 19px;
    color: var(--ink);
  }
  .contact-list li {
    display: flex;
    align-items: center;
    gap: 12px;
    margin-bottom: 8px;
  }
  .contact-icon { width: 22px; height: 22px; flex: none; }

  .wave { position: absolute; inset: 0; width: 100%; height: 100%; }
  .website {
    position: absolute;
    right: 40px;
    bottom: 40px;
    font-family: "Roboto", sans-serif;
    font-size: 18px;
    color: var(--white);
  }
</style>
</head>
<body>

  <section class="card card-front" aria-label="Card front">
    <div class="brand">
      <span class="brand-dot"></span>
      <div class="brand-text">
        <span class="brand-name">Steadforge<br>Path</span>
        <span class="brand-tagline">Life Coaching For Men</span>
      </div>
    </div>
  </section>

  <section class="card card-back" aria-label="Card back">
    <svg class="wave" viewBox="0 0 700 400" preserveAspectRatio="none" aria-hidden="true">
      <path d="M0,318 C240,322 410,270 525,190 C440,280 250,342 0,345 Z" fill="var(--teal)"/>
      <path d="M0,352 C250,352 420,305 530,235 C600,190 650,170 700,160 L700,400 L0,400 Z" fill="var(--navy)"/>
    </svg>

    <h1 class="holder-name"><span class="holder-first">Dale</span> <span class="holder-last">Hartwig</span></h1>

    <div class="brand">
      <span class="brand-dot"></span>
      <div class="brand-text">
        <span class="brand-name">Steadforge<br>Path</span>
        <span class="brand-tagline">Life Coaching For Men</span>
      </div>
    </div>

    <ul class="contact-list">
      <li>
        <svg class="contact-icon" viewBox="0 0 24 24" aria-hidden="true">
          <path d="M6.6 10.8a15 15 0 0 0 6.6 6.6l2.2-2.2a1 1 0 0 1 1-.25 11.4 11.4 0 0 0 3.6.57 1 1 0 0 1 1 1V20a1 1 0 0 1-1 1A17 17 0 0 1 3 4a1 1 0 0 1 1-1h3.5a1 1 0 0 1 1 1c0 1.25.2 2.45.57 3.570a1 1 0 0 1-.25 1z" fill="var(--navy)"/>
        </svg>
        <span>044-555 010 274</span>
      </li>
      <li>
        <svg class="contact-icon" viewBox="0 0 24 24" aria-hidden="true">
          <rect x="2" y="5" width="20" height="14" fill="var(--navy)"/>
          <path d="M2 5l10 8 10-8" fill="none" stroke="var(--white)" stroke-width="1.6"/>
        </svg>
        <span>dale@steadforgepath.com</span>
      </li>
    </ul>

    <p class="website">www.steadforgepath.com</p>
  </section>

</body>
</html>
```